Animal Eye Clinic needs a Business card

We are a new veterinary ophthalmology practice (Tessaly Animal Eye Care) and we need a business card designed. We only see animal eyes - we are not a regular veterinary clinic. We already have a logo. We are looking for a professional, good looking business card to hand out to our clients. We are looking for something simple but professional and contemporary. Our logo is likely the only picture/graphic that needs to be on the card.
Updates

Contact Information for Business Card

Marisol Dunkley, BSc, DVM, MSc, DipACVO
Veterinary Ophthalmologist

Phone: 250.418.3097
Email: tessalyanimaleyecare@mailbrook.net
Website: tessalyanimaleyecare.net
Address: 1840 Pellworth Rd
Kelowna, BC, V4T 8M3

Colors

Designer to choose colors to be used in the design.

Requirements
Must have
• Our logo (attached)

```html
<!DOCTYPE html>
<html lang="en">
<head>
<meta charset="utf-8">
<title>Tessaly Animal Eye Care — Business Card</title>
<link rel="stylesheet" href="https://fonts.googleapis.com/css2?family=Montserrat:wght@400;700;800&family=Quicksand:wght@400;500&display=swap">
<style>
  :root {
    --teal: #1a94a6;
    --grey: #767676;
    --text-grey: #5e5e5e;
    --card: #f7f7f7;
    --stage: #e4e6e7;
  }
  * { box-sizing: border-box; margin: 0; padding: 0; }
  html, body { width: 1200px; height: 900px; overflow: hidden; }
  body {
    background: var(--stage);
    display: flex;
    flex-direction: column;
    align-items: center;
    justify-content: center;
    gap: 30px;
  }
  .card {
    position: relative;
    width: 700px;
    height: 400px;
    background: var(--card);
    overflow: hidden;
    box-shadow: 0 6px 18px rgba(0,0,0,0.12);
  }

  /* Contact side */
  .card-contact .swoosh { position: absolute; inset: 0; }
  .brand-badge {
    position: absolute;
    left: 40px;
    top: 130px;
    width: 200px;
    display: flex;
    flex-direction: column;
    align-items: center;
    gap: 14px;
  }
  .brand-dot { width: 70px; height: 70px; border-radius: 50%; background: var(--teal); }
  .brand-name-small {
    font-family: "Montserrat", sans-serif;
    font-weight: 700;
    font-size: 15px;
    color: var(--teal);
    text-align: center;
    line-height: 1.3;
  }
  .person { position: absolute; left: 355px; top: 44px; }
  .person-name {
    font-family: "Montserrat", sans-serif;
    font-size: 30px;
    letter-spacing: 3px;
    line-height: 1;
  }
  .person-name .first { font-weight: 800; color: var(--teal); }
  .person-name .last { font-weight: 400; color: var(--text-grey); }
  .person-role, .person-creds {
    font-family: "Montserrat", sans-serif;
    font-size: 13px;
    color: var(--text-grey);
    letter-spacing: 0.5px;
    margin-top: 6px;
  }
  .person-creds {
    display: inline-block;
    padding-bottom: 6px;
    border-bottom: 3px solid var(--teal);
    margin-top: 2px;
  }
  .contacts {
    position: absolute;
    left: 380px;
    top: 178px;
    list-style: none;
    display: flex;
    flex-direction: column;
    gap: 14px;
  }
  .contact-row {
    display: flex;
    align-items: center;
    gap: 14px;
    font-family: "Quicksand", sans-serif;
    font-weight: 500;
    font-size: 12.5px;
    color: var(--text-grey);
    letter-spacing: 1.2px;
  }
  .contact-icon {
    flex: none;
    width: 28px;
    height: 28px;
    border-radius: 6px;
    background: var(--teal);
    display: flex;
    align-items: center;
    justify-content: center;
  }
  .contact-icon svg { width: 16px; height: 16px; fill: #fff; }

  /* Brand side */
  .card-brand {
    display: flex;
    flex-direction: column;
    align-items: center;
    justify-content: center;
  }
  .brand-lockup { display: flex; align-items: center; gap: 26px; margin-top: -20px; }
  .brand-lockup .brand-dot { width: 96px; height: 96px; }
  .brand-name-large {
    font-family: "Montserrat", sans-serif;
    font-weight: 700;
    font-size: 34px;
    color: var(--teal);
    line-height: 1.15;
  }
  .brand-url {
    position: absolute;
    bottom: 62px;
    left: 0; right: 0;
    text-align: center;
    font-family: "Quicksand", sans-serif;
    font-weight: 500;
    font-size: 20px;
    letter-spacing: 3px;
    color: var(--teal);
  }
</style>
</head>
<body>

  <section class="card card-contact">
    <svg class="swoosh" viewBox="0 0 700 400" aria-hidden="true">
      <circle cx="95" cy="240" r="270" fill="var(--grey)"/>
      <circle cx="70" cy="200" r="275" fill="var(--teal)"/>
      <circle cx="40" cy="215" r="265" fill="var(--card)"/>
    </svg>

    <div class="brand-badge">
      <div class="brand-dot"></div>
      <p class="brand-name-small">Tessaly Animal<br>Eye Care</p>
    </div>

    <header class="person">
      <h1 class="person-name"><span class="first">MARISOL</span> <span class="last">DUNKLEY</span></h1>
      <p class="person-role">VETERINARY OPHTHALMOLOGIST</p>
      <p class="person-creds">BSC, DVM, MSC, DIPACVO</p>
    </header>

    <ul class="contacts">
      <li class="contact-row">
        <span class="contact-icon"><svg viewBox="0 0 24 24"><path d="M6.6 10.8a15.1 15.1 0 0 0 6.6 6.6l2.2-2.2a1 1 0 0 1 1-.25 11.4 11.4 0 0 0 3.6.57 1 1 0 0 1 1 1V20a1 1 0 0 1-1 1A17 17 0 0 1 3 4a1 1 0 0 1 1-1h3.5a1 1 0 0 1 1 1c0 1.25.2 2.45.57 3.57a1 1 0 0 1-.25 1z"/></svg></span>
        250.418.3097
      </li>
      <li class="contact-row">
        <span class="contact-icon"><svg viewBox="0 0 24 24"><path d="M12 2a7 7 0 0 0-7 7c0 5.25 7 13 7 13s7-7.75 7-13a7 7 0 0 0-7-7zm0 9.5A2.5 2.5 0 1 1 12 6.5a2.5 2.5 0 0 1 0 5z"/></svg></span>
        1840 Pellworth Rd Kelowna, BC, V4T 8M3
      </li>
      <li class="contact-row">
        <span class="contact-icon"><svg viewBox="0 0 24 24"><path d="M3 5h18a1 1 0 0 1 1 1v12a1 1 0 0 1-1 1H3a1 1 0 0 1-1-1V6a1 1 0 0 1 1-1zm9 7.5L4 7.3V8l8 5.2L20 8v-.7z"/></svg></span>
        tessalyanimaleyecare@mailbrook.net
      </li>
      <li class="contact-row">
        <span class="contact-icon"><svg viewBox="0 0 24 24"><path d="M12 2a10 10 0 1 0 0 20 10 10 0 0 0 0-20zm6.9 6h-2.9a15.7 15.7 0 0 0-1.4-3.6A8 8 0 0 1 18.9 8zM12 4c.8 1.2 1.5 2.5 1.9 4h-3.8c.4-1.5 1.1-2.8 1.9-4zM4.3 14a8 8 0 0 1 0-4h3.4a16.5 16.5 0 0 0 0 4zm.8 2h2.9c.3 1.3.8 2.5 1.4 3.6A8 8 0 0 1 5.1 16zM8 8H5.1a8 8 0 0 1 4.3-3.6C8.8 5.5 8.3 6.7 8 8zm4 12c-.8-1.2-1.5-2.5-1.9-4h3.8c-.4 1.5-1.1 2.8-1.9 4zm2.3-6H9.7a14.7 14.7 0 0 1 0-4h4.6a14.7 14.7 0 0 1 0 4zm.3 5.6c.6-1.1 1.1-2.3 1.4-3.6h2.9a8 8 0 0 1-4.3 3.6zm1.7-5.6a16.5 16.5 0 0 0 0-4h3.4a8 8 0 0 1 0 4z"/></svg></span>
        tessalyanimaleyecare.net
      </li>
    </ul>
  </section>

  <section class="card card-brand">
    <div class="brand-lockup">
      <div class="brand-dot"></div>
      <p class="brand-name-large">Tessaly Animal<br>Eye Care</p>
    </div>
    <p class="brand-url">tessalyanimaleyecare.net</p>
  </section>

</body>
</html>
```